Book cover - Quiet Rooms, Open Doors

Book cover for Ebook (Pagelight) and wrap around print cover (Printvale) (back, front, and spine)

The book title (may slightly change by end of brief):
(MAIN TITLE) 'Quiet Rooms, Open Doors'
(SUB HEADING) 'A Week-by-Week Practical Workbook to Loosen Nervous Habits, Quieten Doubt and Build Steady Poise'
by Dr Owen Hartley

I would like a bold, stand out cover. Contemporary. I would like to avoid stereotypical images of people looking anxious or worried. I would like the design to be more uplifting and hopeful, rather than focusing on the negative aspect of anxiety, but avoiding cliched photos of people raising their hands in the air, smiling and jumping etc. The cover should appeal to both men and women.

Trim size of book cover (for PrintVale) is 5.25" x 8" back and front with a spine size of 0.477 inches

Reason: I have decided to extend the deadline by 1 more day, not because I am unhappy with the quality of the designs, but because a few designers have contacted me to explain they have had technical difficulties when submitting their files. Thanks everyone for the hard work and great designs.

Target Market(s)

Males and females (16+) who struggle with social anxiety and shyness

Industry/Entity Type

Social

Font styles to use
Serif

Requirements
Must have
• Bold cover that is modern and contemporary. For example, I like these covers:
• http://shrtlnk.example/k4Tq9Zb
• http://shrtlnk.example/m8Wv2Hn
• http://shrtlnk.example/p3Jx6Lr
• http://shrtlnk.example/t7Gd1Qe
• http://shrtlnk.example/v2Nk8Fy
• http://shrtlnk.example/w9Bh4Cs
• http://shrtlnk.example/z5Mf3Ud
Nice to have
• Open to abstract designs.
Should not have
• No stereotypical pictures of people who look anxious or worried. Avoid cliched photos of people raising their hands in the air, smiling and jumping etc.

```html
<!DOCTYPE html>
<html lang="en">
<head>
<meta charset="utf-8">
<title>Quiet Rooms, Open Doors — Cover</title>
<link rel="stylesheet" href="https://fonts.googleapis.com/css2?family=Oswald:wght@500;700&family=Source+Sans+3:wght@400&display=swap">
<style>
  :root {
    --paper: #ffffff;
    --paper-grain: #e6e6e6;
    --ink-dark: #3b3b3d;
    --ink-red: #d8301f;
    --ink-red-deep: #b8251a;
    --ink-teal: #1f9cc4;
    --shadow: rgba(0, 0, 0, 0.22);
  }
  * { margin: 0; padding: 0; box-sizing: border-box; }
  html, body { width: 788px; height: 1200px; overflow: hidden; background: var(--paper); }
  .cover {
    position: relative;
    width: 788px;
    height: 1200px;
    overflow: hidden;
    background:
      radial-gradient(ellipse at 50% 50%, var(--paper) 55%, transparent 80%),
      radial-gradient(circle at 10% 8%, var(--paper-grain) 0, transparent 22%),
      radial-gradient(circle at 92% 14%, var(--paper-grain) 0, transparent 20%),
      radial-gradient(circle at 6% 88%, var(--paper-grain) 0, transparent 22%),
      radial-gradient(circle at 94% 92%, var(--paper-grain) 0, transparent 22%),
      var(--paper);
  }
  .title {
    position: absolute;
    left: 0;
    top: 44px;
    width: 100%;
    text-align: center;
    font-family: "Oswald", sans-serif;
    font-weight: 700;
    text-transform: uppercase;
    line-height: 1;
  }
  .title-line { display: block; }
  .title-line--first { color: var(--ink-dark); font-size: 108px; letter-spacing: 6px; }
  .title-line--accent { color: var(--ink-red); font-size: 108px; letter-spacing: 4px; margin-top: 16px; }
  .title-line--last { color: var(--ink-dark); font-size: 108px; letter-spacing: 5px; margin-top: 16px; }
  .subtitle {
    position: absolute;
    left: 110px;
    top: 448px;
    width: 568px;
    text-align: center;
    font-family: "Source Sans 3", sans-serif;
    font-weight: 400;
    font-size: 25px;
    line-height: 33px;
    color: var(--ink-teal);
  }
  .artwork {
    position: absolute;
    left: 113px;
    top: 566px;
    width: 565px;
    height: 405px;
    border-radius: 48% 52% 46% 50% / 55% 58% 42% 45%;
    background: radial-gradient(ellipse at 50% 45%, var(--ink-red) 0%, var(--ink-red-deep) 100%);
  }
  .artwork-shadow {
    position: absolute;
    left: 240px;
    top: 990px;
    width: 310px;
    height: 30px;
    border-radius: 50%;
    background: radial-gradient(ellipse at center, var(--shadow) 0%, transparent 70%);
  }
  .author {
    position: absolute;
    left: 0;
    top: 1112px;
    width: 100%;
    text-align: center;
    font-family: "Oswald", sans-serif;
    font-weight: 500;
    font-size: 54px;
    letter-spacing: 1px;
    text-transform: uppercase;
    color: var(--ink-dark);
    line-height: 1;
  }
</style>
</head>
<body>
  <main class="cover">
    <h1 class="title">
      <span class="title-line title-line--first">Quiet Rooms,</span>
      <span class="title-line title-line--accent">Open</span>
      <span class="title-line title-line--last">Doors</span>
    </h1>
    <p class="subtitle">A Week-by-Week Practical Workbook to Loosen Nervous Habits, Quieten Doubt and Build Steady Poise</p>
    <div class="artwork" role="img" aria-label="Brain-shaped word cloud of feeling words in red, with one highlighted word in teal at its centre"></div>
    <div class="artwork-shadow"></div>
    <p class="author">Dr Owen Hartley</p>
  </main>
</body>
</html>
```